Golden Petal Circle (postcard)/ Lumora Vive Medspa and Wellness (company name)

Front of card
Marion Castellane picture, name of our company, and the quote by Marion Castellane.

Back of card
Golden Petal Circle
(attached is how it works in a word document)

It Company

```html
<!DOCTYPE html>
<html lang="en">
<head>
<meta charset="utf-8">
<title>Golden Petal Circle Postcard – Lumora Vive Medspa and Wellness</title>
<link rel="stylesheet" href="https://fonts.googleapis.com/css2?family=Great+Vibes&family=Lato:wght@400;700&family=Playfair+Display:ital,wght@0,400;0,700;1,400&display=swap">
<style>
  :root {
    --page: #ffffff;
    --mauve-light: #e9d3d3;
    --mauve: #c9a3a6;
    --mauve-deep: #9c7479;
    --plum: #5b3f5e;
    --plum-dark: #3e2a40;
    --lilac: #cdb7d6;
    --tier: #8d6a9a;
    --tier-dark: #6f4f7e;
    --ink: #3a2b2e;
    --gold: #b98a4a;
    --white: #ffffff;
    --card-shadow: rgba(60, 40, 50, 0.25);
  }
  * { box-sizing: border-box; margin: 0; padding: 0; }
  html, body {
    width: 900px; height: 1200px; overflow: hidden;
    background: var(--page);
    font-family: "Lato", sans-serif;
    color: var(--ink);
  }
  .canvas { position: relative; width: 900px; height: 1200px; }

  .postcard {
    position: absolute; left: 24px; width: 852px;
    overflow: hidden;
    box-shadow: 0 2px 6px var(--card-shadow);
  }

  /* FRONT */
  .postcard--front {
    top: 12px; height: 572px;
    background: linear-gradient(100deg, var(--mauve-deep) 0%, var(--mauve) 35%, var(--mauve-light) 60%, var(--mauve) 100%);
  }
  .front__portrait {
    position: absolute; left: 0; top: 0; width: 360px; height: 572px;
    background: linear-gradient(180deg, #4a3a3d 0%, #7d5e62 30%, #c9a3a6 60%, #8a5f66 100%);
  }
  .front__portrait-faded {
    position: absolute; right: 0; top: 120px; width: 300px; height: 452px;
    background: radial-gradient(ellipse at 55% 45%, rgba(90,60,66,0.55) 0%, rgba(201,163,166,0.2) 60%, transparent 80%);
  }
  .brand {
    position: absolute; right: 40px; top: 26px; text-align: right;
    display: flex; align-items: center; gap: 12px;
  }
  .brand__name {
    font-family: "Playfair Display", serif; font-weight: 700;
    font-size: 30px; line-height: 1.1; color: var(--white);
  }
  .brand__dot { width: 18px; height: 18px; border-radius: 50%; background: var(--gold); }

  .quote {
    position: absolute; left: 380px; top: 165px; width: 250px;
    font-family: "Playfair Display", serif; font-size: 25px; line-height: 1.3;
    color: var(--ink);
  }
  .quote__author {
    display: block; margin-top: 10px; text-align: right;
    font-family: "Great Vibes", cursive; font-size: 20px; color: var(--plum-dark);
  }

  /* BACK */
  .postcard--back {
    top: 612px; height: 570px; background: var(--white);
  }
  .back__program {
    position: absolute; left: 0; top: 0; width: 540px; height: 570px;
    background: linear-gradient(160deg, #e9dce6 0%, var(--lilac) 45%, #e6cdd0 100%);
    padding: 14px 20px;
  }
  .program__title {
    font-family: "Great Vibes", cursive; font-size: 36px; color: var(--plum);
    margin-left: 110px;
  }
  .program__intro {
    font-size: 12.5px; line-height: 1.45; color: var(--plum-dark);
    font-style: italic; margin-top: 4px;
  }
  .program__question {
    margin-top: 12px; text-align: center; font-size: 15px; color: var(--plum-dark);
  }
  .program__question strong { color: var(--plum); }
  .tiers { display: flex; gap: 6px; margin-top: 10px; }
  .tier {
    flex: 1; background: rgba(141,106,154,0.75); color: var(--white);
    padding: 8px 8px; font-size: 10.5px; line-height: 1.35; min-height: 250px;
  }
  .tier__head { font-weight: 700; font-size: 11.5px; margin-bottom: 4px; border-bottom: 1px solid rgba(255,255,255,0.5); padding-bottom: 3px; }
  .tier ul { list-style: none; }
  .tier li::before { content: "• "; }
  .tier li.sub { padding-left: 10px; }
  .tier li.sub::before { content: "** "; }
  .tier li .note { font-size: 8.5px; opacity: 0.9; }
  .program__footnote { font-size: 9.5px; color: var(--plum-dark); margin-top: 8px; line-height: 1.4; }
  .program__rule {
    text-align: center; font-size: 10px; font-weight: 700; letter-spacing: 0.5px;
    color: var(--plum); margin-top: 6px;
  }
  .stamp-box {
    position: absolute; right: 44px; top: 68px; width: 64px; height: 70px;
    border: 2px solid var(--tier-dark);
  }
</style>
</head>
<body>
<main class="canvas">

  <section class="postcard postcard--front" aria-label="Postcard front">
    <div class="front__portrait" role="img" aria-label="Portrait photograph of Marion Castellane"></div>
    <div class="front__portrait-faded" role="img" aria-label="Faded second portrait of Marion Castellane"></div>
    <div class="brand">
      <span class="brand__name">Lumora Vive<br>Medspa &amp; Wellness</span>
      <span class="brand__dot"></span>
    </div>
    <blockquote class="quote">
      “As you grow older, you will discover that you have two hands, one for helping yourself, the other for helping others.”
      <cite class="quote__author">Marion Castellane</cite>
    </blockquote>
  </section>

  <section class="postcard postcard--back" aria-label="Postcard back">
    <div class="back__program">
      <h1 class="program__title">Golden Petal Circle</h1>
      <p class="program__intro">At Lumora Vive, the greatest compliment we can receive is a referral from one of our valued guests! Simply refer a new guest, who mentions your name when scheduling their first appointment, and watch your rewards flourish. Lumora Vive’s gift is here for you!</p>
      <p class="program__question">What does the program do for you? <strong>We are so happy you asked!</strong></p>
      <div class="tiers">
        <div class="tier">
          <div class="tier__head">After 3 Referrals</div>
          <ul>
            <li>Lumora Vive Facial</li>
            <li>LumaPeel</li>
            <li>Laser Reduction <span class="note">(3 sessions)*</span></li>
            <li class="sub">Happy trail</li>
            <li class="sub">Chin or lip</li>
            <li class="sub">Eyebrows</li>
            <li class="sub">Underarms</li>
          </ul>
        </div>
        <div class="tier">
          <div class="tier__head">After 6 Referrals</div>
          <ul>
            <li>12 units of Velaxa</li>
            <li>Microdermabrasion <span class="note">(face or chest)</span></li>
            <li>Hydrating SoftGlow Peel</li>
            <li>TCA Chemical Peel</li>
            <li>Laser Reduction <span class="note">(3 sessions)*</span></li>
            <li class="sub">Bikini line</li>
            <li class="sub">Upper or Lower back</li>
            <li class="sub">Forearms</li>
            <li class="sub">Shoulders</li>
          </ul>
        </div>
        <div class="tier">
          <div class="tier__head">After 9 Referrals</div>
          <ul>
            <li>25 units of Velaxa</li>
            <li>$200 off of a Filler <span class="note">(excludes Contoura)</span></li>
            <li>Vera Peel</li>
            <li>IPL Photofacial <span class="note">(face, neck &amp; chest)</span></li>
            <li>Microneedling with Cellura <span class="note">(face only)</span></li>
            <li>Spider Vein treatments <span class="note">(one area)</span></li>
            <li>Laser Reduction <span class="note">(3 sessions)*</span></li>
            <li class="sub">Brazilian</li>
            <li class="sub">Lower legs OR Upper legs</li>
            <li class="sub">Whole arm</li>
            <li class="sub">Full face</li>
          </ul>
        </div>
      </div>
      <p class="program__footnote">* Choose one<br>** Choose one</p>
      <p class="program__rule">REFERRED CLIENT PURCHASE IS NECESSARY</p>
    </div>
    <div class="stamp-box" aria-label="Stamp area"></div>
  </section>

</main>
</body>
</html>
```